Launching new podcast and need artwork

we are two guys in our early 40's from east Texas who are starting a podcast around personal finance.

The title of the podcast will be "Coin Porchlight" and the subtitle will be "Money tricks with a little front-porch drawl"

We own the company brightharborplans.com and will be using the podcast as a lead generation for our primary business of financial coaching.

Target Market(s)

Male 35-45 years old

Industry/Entity Type

Personal finance

Requirements
Nice to have
• Rugged or rustic feel would fit our personas

```html
<!DOCTYPE html>
<html lang="en">
<head>
<meta charset="utf-8">
<title>Coin Porchlight – Podcast Cover</title>
<link rel="stylesheet" href="https://fonts.googleapis.com/css2?family=Oswald:wght@700&family=Saira+Semi+Condensed:wght@600;700&display=swap">
<style>
  :root {
    --backdrop: #d9dadc;
    --night: #15110b;
    --amber-deep: #5a3a0c;
    --amber: #c98a1f;
    --gold: #f2c94c;
    --gold-soft: #f4d26a;
    --band-black: #1a1411;
    --silver-top: #ffffff;
    --silver-bottom: #c9ccd0;
    --wood-dark: #3f3b33;
    --wood-light: #7b776a;
    --white: #ffffff;
  }
  * { margin: 0; padding: 0; box-sizing: border-box; }
  html, body {
    width: 1200px;
    height: 1177px;
    overflow: hidden;
    background: var(--backdrop);
  }
  .cover {
    position: absolute;
    left: 200px;
    top: 188px;
    width: 800px;
    height: 800px;
    overflow: hidden;
    background: var(--night);
  }
  .cover__scene {
    position: absolute;
    inset: 0 0 300px 0;
    background:
      radial-gradient(ellipse 55% 60% at 50% 42%, var(--gold) 0%, var(--amber) 35%, transparent 70%),
      radial-gradient(ellipse 50% 60% at 95% 50%, var(--amber) 0%, transparent 70%),
      linear-gradient(180deg, var(--night) 0%, var(--amber-deep) 100%);
  }
  .cover__floor {
    position: absolute;
    left: 0; right: 0; bottom: 0;
    height: 300px;
    background: linear-gradient(180deg, var(--wood-light) 0%, var(--wood-dark) 100%);
  }
  .cover__banner {
    position: absolute;
    inset: 0;
    width: 800px;
    height: 800px;
  }
  .banner__title {
    font-family: "Oswald", sans-serif;
    font-weight: 700;
    font-size: 92px;
  }
  .banner__title-light { fill: url(#silver); }
  .banner__title-gold { fill: var(--gold-soft); }
  .cover__tagline {
    position: absolute;
    right: 26px;
    top: 680px;
    text-align: right;
    font-family: "Saira Semi Condensed", sans-serif;
    line-height: 1.05;
  }
  .tagline__lead {
    display: block;
    color: var(--gold);
    font-weight: 700;
    font-size: 44px;
    letter-spacing: 0.5px;
    text-shadow: 0 2px 4px rgba(0,0,0,0.6);
  }
  .tagline__rest {
    display: block;
    color: var(--white);
    font-weight: 600;
    font-size: 36px;
    text-shadow: 0 2px 4px rgba(0,0,0,0.6);
  }
</style>
</head>
<body>
  <main class="cover">
    <div class="cover__scene" role="img" aria-label="Golden tree made of coins glowing against a dark sky, with coins falling around it"></div>
    <div class="cover__floor" role="img" aria-label="Weathered rustic wooden planks forming a floor"></div>

    <svg class="cover__banner" viewBox="0 0 800 800">
      <defs>
        <linearGradient id="silver" x1="0" y1="0" x2="0" y2="1">
          <stop offset="0" stop-color="#ffffff"/>
          <stop offset="1" stop-color="#c9ccd0"/>
        </linearGradient>
      </defs>
      <polygon class="banner__gold" points="0,542 800,402 800,550 0,704" fill="var(--gold)"/>
      <polygon class="banner__black" points="0,530 690,410 705,560 0,688" fill="var(--band-black)"/>
      <g class="banner__arrows" fill="var(--band-black)">
        <polygon points="722,462 744,478 722,494"/>
        <polygon points="744,458 766,474 744,490"/>
        <polygon points="766,454 788,470 766,486"/>
      </g>
      <text class="banner__title" x="40" y="648" transform="rotate(-10 40 648)" textLength="600" lengthAdjust="spacingAndGlyphs">
        <tspan class="banner__title-light">COIN</tspan><tspan class="banner__title-gold" dx="16">PORCHLIGHT</tspan>
      </text>
    </svg>

    <p class="cover__tagline">
      <span class="tagline__lead">MONEY TRICKS</span>
      <span class="tagline__rest">with a little front-porch drawl</span>
    </p>
  </main>
</body>
</html>
```